Drolbix Overview and Demo Presentation

Objective:
Create a bold, visually engaging PowerPoint deck to present Drolbix’s sales process and system demo to local movers, emphasizing ease of use, increased profitability, and operational efficiency.
Key Elements:
• Design: High-impact graphics with Drolbix branding, minimal text, and clean layouts.
• Content: Step-by-step sales process, key selling points, system demo walkthrough, and a compelling call-to-action.
• Live Demo: Showcase Drolbix’s platform, focusing on instant guaranteed pricing, streamlined booking, and support features.
Deliverables:
A dynamic presentation designed to educate and convert local movers into Drolbix partners, ensuring seamless flow and strong audience engagement.

Target Market(s)

Local Movers

Industry/Entity Type

Household Goods Moving

Font styles to use
Sans Serif

Colors
0054AA
0677BA
7BADD7
CADEEF
E8F1F8
FFC000
F8CF3A
FAE287
FDF2CF
FEFAEE

Requirements
Must have
• Project Brief: Drolbix Sales Process Presentation Objective: Create a bold, visually engaging PowerPoint deck to present Drolbix’s sales process and system demo to local movers, emphasizing ease of use, increased profitability, and operational efficiency. Key Elements: • Design: High-impact graphics with Drolbix branding, minimal text, and clean layouts. • Content: Step-by-step sales process, key selling points, system demo walkthrough, and a compelling call-to-action. • Live Demo: Showcase Drolbix’s platform, focusing on instant guaranteed pricing, streamlined booking, and support features. Deliverables: A dynamic presentation designed to educate and convert local movers into Drolbix partners, ensuring seamless flow and strong audience engagement.

```html
<!DOCTYPE html>
<html lang="en">
<head>
<meta charset="utf-8">
<title>Drolbix Partner Overview Deck</title>
<link href="https://fonts.googleapis.com/css2?family=Lato:wght@400;700;900&display=swap" rel="stylesheet">
<style>
:root{
  --blue:#2d5be3;
  --blue-deep:#2550d2;
  --yellow:#fcc74f;
  --ink:#1b1b1f;
  --text:#3d3f46;
  --muted:#5a5d66;
  --paper:#ffffff;
  --pale:#eef3fd;
}
*{box-sizing:border-box;margin:0;padding:0}
html,body{width:1050px;height:1200px;overflow:hidden;background:var(--paper)}
body{font-family:'Lato',sans-serif;color:var(--ink);position:relative}
.slide{position:absolute;width:454px;height:255px;background:var(--paper);overflow:hidden;box-shadow:0 1px 4px rgba(0,0,0,.12)}
.slide--blue{background:linear-gradient(180deg,#3567e8 0%,#2b58dd 60%,#2a55d6 100%)}
.abs{position:absolute}
.center{left:0;right:0;text-align:center}
.blue{color:var(--blue)}
.yellow{color:var(--yellow)}
.foot{position:absolute;left:0;right:0;bottom:0;height:14px;background:var(--yellow);font-size:5.5px;color:#333}
.foot-brand{position:absolute;left:13px;top:0;width:64px;height:14px;background:#fff;display:flex;align-items:center;justify-content:center;gap:3px;font-weight:900;font-size:8.5px;color:var(--blue)}
.foot-brand i{width:5px;height:5px;background:var(--blue);display:block}
.foot-url{position:absolute;left:0;right:0;top:4px;text-align:center}
.foot-page{position:absolute;right:10px;top:4px}
.mark{display:inline-block;width:9px;height:9px;background:var(--blue);margin-right:6px;vertical-align:middle}
.heading{font-weight:700;font-size:17px;line-height:1}
.photo{position:absolute}
.brand-xl{font-weight:900;font-size:34px;color:#fff;letter-spacing:1.5px;display:flex;align-items:center;justify-content:center;gap:12px}
.stat{position:absolute;width:130px;height:72px;text-align:center;display:flex;flex-direction:column;justify-content:center;align-items:center}
.stat--y{background:var(--yellow)}
.stat--b{background:var(--blue)}
.stat b{font-size:17px;font-weight:700;line-height:1.1}
.stat span{font-size:8.5px;line-height:1.3;margin-top:3px;color:#fff;padding:0 10px}
.stat--y b{color:var(--blue)}
.stat--b b{color:var(--yellow)}
.label-sm{position:absolute;width:130px;text-align:center;font-size:9px;font-weight:700}
.about p{font-size:8.8px;line-height:14.1px;color:var(--ink)}
.step{position:absolute;width:100px;margin-left:-50px;text-align:center}
.step h4{font-size:7.8px;color:var(--blue);font-weight:700;white-space:nowrap}
.step p{font-size:5.4px;line-height:7.8px;color:var(--text);margin-top:6px}
.feature{position:absolute;left:203px;width:240px}
.feature h4{font-size:8.5px;line-height:10px;color:var(--yellow);font-weight:700}
.feature p{font-size:6px;line-height:8.8px;color:var(--text);margin-top:2px}
.col{position:absolute;width:131px;text-align:center}
.col h4{font-size:10px;color:var(--yellow);font-weight:700}
.col h5{font-size:6px;line-height:8.5px;color:var(--blue);font-weight:700;margin-top:4px}
.col p{font-size:5.7px;line-height:8.2px;color:var(--text);margin-top:6px}
.contact{position:absolute;display:flex;gap:6px;align-items:flex-start;color:#fff;font-size:9px;line-height:13px}
</style>
</head>
<body>

<section class="slide slide--blue" style="left:51px;top:41px">
  <div class="photo" role="img" aria-label="Faded photo of a semi truck on a highway with mountains behind" style="inset:0 0 14px 0;background:linear-gradient(180deg,rgba(255,255,255,.06) 0%,rgba(20,50,160,.18) 100%)"></div>
  <div class="abs center brand-xl" style="top:62px">Drolbix</div>
  <div class="abs center" style="top:124px;color:#fff;font-size:23px;font-weight:700">Moving For The Next Generation</div>
  <div class="abs center" style="top:160px;color:#fff;font-size:10.5px">Partner Overview Presentation</div>
  <footer class="foot"><div class="foot-brand"><i></i>Drolbix</div><div class="foot-url">Drolbix.com</div><div class="foot-page">Page No : 01</div></footer>
</section>

<section class="slide" style="left:547px;top:41px">
  <div class="abs center heading" style="top:18px;line-height:21px;font-size:18px">Revolutionizing <span class="blue">The Moving</span><br><span class="blue">Industry With Ai</span></div>
  <div class="stat stat--y" style="left:9px;top:53px"><b>$1.9M</b><span>Revenue Successfully Raised</span></div>
  <div class="label-sm" style="left:9px;top:135px">To Build</div>
  <div class="stat stat--b" style="left:9px;top:155px"><b>$5</b><span>Appraised Tech Stack</span></div>
  <div class="stat stat--y" style="left:314px;top:53px"><b>$500K</b><span>AdditionalRaise</span></div>
  <div class="label-sm" style="left:314px;top:135px">To Prove</div>
  <div class="stat stat--b" style="left:314px;top:155px"><b>B21</b><span>Successful Model</span></div>
  <svg class="abs" style="left:0;top:0" width="454" height="255">
    <g stroke="var(--blue)" stroke-width=".8" stroke-dasharray="2 2"><line x1="74" y1="125" x2="74" y2="134"/><line x1="379" y1="125" x2="379" y2="134"/></g>
    <g stroke="var(--yellow)" stroke-width=".8" stroke-dasharray="2 2"><line x1="74" y1="147" x2="74" y2="155"/><line x1="379" y1="147" x2="379" y2="155"/></g>
  </svg>
  <div class="abs center" style="top:94px;font-size:14px;font-weight:700;color:var(--blue)">Proven Model</div>
  <p class="abs" style="left:160px;width:134px;top:124px;font-size:6.6px;line-height:10.6px;text-align:center;color:var(--text)">Drolbix is transforming the $90-100B moving industry by leveraging AI, GPS, and automated compliance to deliver the first instant guaranteed pricing platform. We're cutting out inefficiencies and middlemen to improve costs and service quality</p>
  <footer class="foot"><div class="foot-brand"><i></i>Drolbix</div><div class="foot-url">Drolbix.com</div><div class="foot-page">Page No : 05</div></footer>
</section>

<section class="slide about" style="left:50px;top:329px">
  <svg class="abs" style="left:0;top:0" width="454" height="255">
    <polygon points="188,0 428,0 308,125" fill="var(--blue)"/>
    <polygon points="194,0 420,0 308,117" fill="#fff"/>
    <polyline points="453,2 331,122 453,240" fill="none" stroke="var(--yellow)" stroke-width="7"/>
    <polyline points="453,14 345,122 453,228" fill="none" stroke="var(--blue)" stroke-width="6"/>
    <polygon points="453,24 453,220 356,122" fill="var(--blue)"/>
  </svg>
  <div class="photo" role="img" aria-label="Smiling couple carrying moving boxes in a bright home" style="left:0;top:0;width:454px;height:125px;background:linear-gradient(135deg,#d9d4cb,#b8aa96);clip-path:polygon(199px 0,416px 0,308px 112px)"></div>
  <div class="abs heading" style="left:14px;top:27px;font-size:18px"><span class="mark" style="width:11px;height:11px"></span>About <span class="blue">Us</span></div>
  <p class="abs" style="left:14px;top:58px;width:216px"><span class="blue">Drolbix</span> is the next logical evolution in professional moving. Professional moving clients have battled soaring prices, acute capacity problems and deteriorating service levels.</p>
  <p class="abs" style="left:14px;top:129px;width:268px"><span class="blue">Drolbix</span> was founded by lifelong moving professionals who have developed the answer to better moving services. Poised as THE industry disruptor, we deliver faster, offer guaranteed prices and even offer no credit check financing options. We are a technology first organization using proprietary software to deliver moving's best service experience.</p>
  <footer class="foot"><div class="foot-brand"><i></i>Drolbix</div><div class="foot-url">Drolbix.com</div><div class="foot-page">Page No : 02</div></footer>
</section>

<section class="slide" style="left:547px;top:329px">
  <div class="photo slide--blue" role="img" aria-label="Blue-tinted photo of movers at work" style="left:0;top:0;width:454px;height:112px"></div>
  <div class="abs center heading" style="top:28px;color:#fff;font-size:18px;line-height:21px">The Solution – Drolbix's AI-Powered<br>Platform</div>
  <svg class="abs" style="left:0;top:0" width="454" height="255">
    <g fill="none" stroke="#9a9a9a" stroke-width=".7" stroke-dasharray="2 1.5">
      <path d="M30,111 A26,26 0 0 0 82,111"/><line x1="56" y1="137" x2="56" y2="164"/>
      <path d="M146,111 A26,26 0 0 0 198,111"/><line x1="172" y1="137" x2="172" y2="164"/>
      <path d="M255,111 A26,26 0 0 0 307,111"/><line x1="281" y1="137" x2="281" y2="164"/>
      <path d="M371,111 A26,26 0 0 0 423,111"/><line x1="397" y1="137" x2="397" y2="164"/>
    </g>
    <g fill="var(--yellow)"><circle cx="56" cy="111" r="20"/><circle cx="172" cy="111" r="20"/><circle cx="281" cy="111" r="20"/><circle cx="397" cy="111" r="20"/></g>
    <g fill="var(--blue)" font-family="Lato,sans-serif" font-weight="700" font-size="17" text-anchor="middle">
      <text x="56" y="117">01</text><text x="172" y="117">02</text><text x="281" y="117">03</text><text x="397" y="117">04</text>
    </g>
  </svg>
  <div class="step" style="left:56px;top:171px"><h4>Cutting Out Middlemen</h4><p>Drolbix directly connects customers with local movers, eliminating van lines, brokers, and agents. This streamlines the process and ensures transparent, fair pricing.</p></div>
  <div class="step" style="left:172px;top:171px"><h4>AI-Driven Instant Pricing</h4><p>Drolbix offers the industry's only instant, guaranteed pricing using AI, GPS, and key moving variables.</p></div>
  <div class="step" style="left:281px;top:171px"><h4>Automated Compliance</h4><p>Fully automates interstate regulatory compliance, reducing legal risks for all movers in the supply chain.</p></div>
  <div class="step" style="left:397px;top:171px"><h4>Real-Time Capacity Matching</h4><p>The platform optimizes truck capacity by matching real-time availability with customer move requests, improving operational efficiency.</p></div>
  <footer class="foot"><div class="foot-brand"><i></i>Drolbix</div><div class="foot-url">Drolbix.com</div><div class="foot-page">Page No : 06</div></footer>
</section>

<section class="slide" style="left:51px;top:616px">
  <svg class="abs" style="left:0;top:0" width="454" height="255">
    <path d="M0,9 A112,112 0 0 1 65.9,30.4 L41.2,64.4 A70,70 0 0 0 0,51 Z" fill="var(--blue)"/>
    <path d="M65.9,30.4 A112,112 0 0 1 106.5,86.4 L66.6,99.4 A70,70 0 0 0 41.2,64.4 Z" fill="var(--yellow)"/>
    <path d="M106.5,86.4 A112,112 0 0 1 106.5,155.6 L66.6,142.6 A70,70 0 0 0 66.6,99.4 Z" fill="var(--blue)"/>
    <path d="M106.5,155.6 A112,112 0 0 1 65.9,211.6 L41.2,177.6 A70,70 0 0 0 66.6,142.6 Z" fill="var(--yellow)"/>
    <path d="M65.9,211.6 A112,112 0 0 1 0,233 L0,191 A70,70 0 0 0 41.2,177.6 Z" fill="var(--blue)"/>
    <circle cx="23" cy="121" r="12" fill="var(--yellow)"/>
    <g fill="none" stroke-width="1.2">
      <g stroke="#fff"><rect x="15" y="36" width="16" height="5" rx="2"/><rect x="15" y="45" width="16" height="5" rx="2"/></g>
      <g stroke="var(--blue)"><circle cx="78" cy="60" r="4.5"/><path d="M69,75 a9,7 0 0 1 18,0 Z"/></g>
      <g stroke="#fff"><circle cx="100" cy="118" r="5"/><path d="M88,130 l6,-3 h8 l6,-4"/></g>
      <g stroke="var(--blue)"><circle cx="78" cy="179" r="5"/><line x1="82" y1="183" x2="87" y2="188"/></g>
      <g stroke="#fff"><circle cx="26" cy="197" r="5"/><rect x="15" y="200" width="6" height="9"/></g>
    </g>
  </svg>
  <div class="abs heading" style="left:176px;top:16px;font-size:18px"><span class="mark" style="width:11px;height:11px"></span>Drolbix <span class="blue">Solution</span></div>
  <svg class="abs" style="left:170px;top:50px" width="26" height="180" fill="none" stroke="var(--blue)" stroke-width="1">
    <rect x="3" y="3" width="16" height="5" rx="2"/><rect x="3" y="11" width="16" height="5" rx="2"/>
    <circle cx="11" cy="43" r="4"/><path d="M3,56 a8,6 0 0 1 16,0 Z"/>
    <circle cx="12" cy="80" r="4"/><path d="M2,91 l6,-3 h8 l6,-4"/>
    <circle cx="10" cy="117" r="5"/><line x1="14" y1="121" x2="19" y2="126"/>
    <circle cx="14" cy="156" r="5"/><rect x="3" y="159" width="6" height="9"/>
  </svg>
  <div class="feature" style="top:52px"><h4>On-Demand Process</h4><p>Drolbix automatically audits: Compliance, Insurance, Regulatory, Bonding, Background checks, and Quality.</p></div>
  <div class="feature" style="top:89px"><h4>One Point of Contact</h4><p>Today moves are sold from broker to broker until it's finally sold to a mover. Many entities involved means a confusing line of correspondence for the customer.</p></div>
  <div class="feature" style="top:126px"><h4>Book Now Pay Later</h4><p>Moving has a high price tag, but no one has ever offered a pay later solution. Much less a no credit check offer.</p></div>
  <div class="feature" style="top:164px"><h4>GPS Tracking</h4><p>Big retailers have conditioned consumers to expect real-time tracking of goods. Only Drolbix enables you to track all of your belongings door to door.</p></div>
  <div class="feature" style="top:203px"><h4>Simple Honest Pricing</h4><p>Drolbix's proprietary algorithms and data are backed up by a checks and balances process giving the first instant pricing solution that won't change.</p></div>
  <footer class="foot"><div class="foot-brand"><i></i>Drolbix</div><div class="foot-url">Drolbix.com</div><div class="foot-page">Page No : 03</div></footer>
</section>

<section class="slide" style="left:547px;top:616px">
  <div class="abs" style="left:16px;top:14px;width:196px;height:214px;background:linear-gradient(90deg,var(--pale),#fff 50%,var(--pale))"></div>
  <div class="photo" role="img" aria-label="Desktop monitor displaying the white label moving website" style="left:22px;top:47px;width:185px;height:155px;background:linear-gradient(180deg,#1d1d1f 0%,#3b3630 62%,#d9dbe0 62%,#eef0f3 100%);border-radius:4px"></div>
  <div class="abs heading" style="left:236px;top:24px;font-size:18px"><span class="mark" style="width:11px;height:11px"></span>Drolbix <span class="blue">White Label</span></div>
  <p class="abs" style="left:235px;top:56px;width:170px;font-size:8.5px;line-height:10.6px;font-weight:700;color:var(--yellow)">Partner with Drolbix and take advantage of our cutting-edge technology to gain a competitive edge in the industry.</p>
  <p class="abs" style="left:235px;top:96px;width:202px;font-size:8.3px;line-height:11.8px;color:var(--ink)">Drolbix offers a white labeling solution for companies looking to capture direct moves. Our technology platform can be customized with your branding to provide a seamless integration with your existing systems and processes. This allows you to offer a top-notch interstate moving experience to your customers, while leveraging the power of Drolbix's proven technology. With this solution, you can streamline your operations, increase customer satisfaction, and capture more business in the lucrative long-distance move market.</p>
  <footer class="foot"><div class="foot-brand"><i></i>Drolbix</div><div class="foot-url">Drolbix.com</div><div class="foot-page">Page No : 07</div></footer>
</section>

<section class="slide" style="left:51px;top:904px">
  <div class="abs center heading" style="top:21px;font-size:18px"><span class="mark" style="width:11px;height:11px"></span>Our <span class="blue">Vision</span></div>
  <div class="photo" role="img" aria-label="City skyline with glass towers" style="left:16px;top:53px;width:131px;height:89px;background:linear-gradient(180deg,#b9cde2,#6f8aa2 70%,#4d5f48)"></div>
  <div class="photo" role="img" aria-label="Room stacked with cardboard moving boxes" style="left:162px;top:53px;width:131px;height:89px;background:linear-gradient(180deg,#e7e3dc,#b7916a 75%,#8d6a48)"></div>
  <div class="photo" role="img" aria-label="Two colleagues packing a box in an office" style="left:308px;top:53px;width:131px;height:89px;background:linear-gradient(135deg,#4a4f57,#a89c8c 60%,#d8d0c4)"></div>
  <div class="col" style="left:16px;top:149px"><h4>Our Vision</h4><h5>Revolutionize the moving industry by providing great value to everyone involved</h5><p>Drolbix Customers - Consumers, Movers, Corporate Clients, and Relocation Management Companies all receive better value with Drolbix than anywhere else.</p></div>
  <div class="col" style="left:162px;top:149px"><h4>Our Mission</h4><h5>Disrupt a $86B sleepy giant of an inefficient industry</h5><p>Drolbix's deep understanding of the professional moving industry, supported by extensive market research has set Drolbix up for ultimate success in disrupting this industry by creating cost-saving efficiencies throughout.</p></div>
  <div class="col" style="left:308px;top:149px"><h4>Our Goal</h4><h5>Becoming the moving platform of choice</h5><p>As Drolbix's market share grows, the customer acquisition cost and operational cost plummets. This creates even more market penetration, more efficiencies, and exponential growth.</p></div>
  <footer class="foot"><div class="foot-brand"><i></i>Drolbix</div><div class="foot-url">Drolbix.com</div><div class="foot-page">Page No : 04</div></footer>
</section>

<section class="slide slide--blue" style="left:547px;top:904px">
  <div class="photo" role="img" aria-label="Faded photo of a semi truck on a highway" style="inset:0 0 14px 0;background:linear-gradient(180deg,rgba(255,255,255,.05),rgba(20,50,160,.18))"></div>
  <div class="abs center brand-xl" style="top:55px">Drolbix</div>
  <div class="abs center" style="top:118px;color:#fff;font-size:23px;font-weight:700">Thank You</div>
  <div class="contact" style="left:32px;top:170px">
    <svg width="11" height="14" viewBox="0 0 11 14" fill="none" stroke="#fff" stroke-width="1"><path d="M5.5,13 C2,8.5 1,6.5 1,5 a4.5,4.5 0 0 1 9,0 c0,1.5 -1,3.5 -4.5,8 Z"/><circle cx="5.5" cy="5" r="1.6"/></svg>
    <span>480 W. Larkmoor Ave., #210C<br>Fairhaven City, ST 00000</span>
  </div>
  <div class="contact" style="left:200px;top:170px">
    <svg width="13" height="13" viewBox="0 0 13 13" fill="none" stroke="#fff" stroke-width="1"><path d="M2,1 l2.5,0 l1,3 l-1.5,1 a7,7 0 0 0 3.5,3.5 l1,-1.5 l3,1 l0,2.5 a1,1 0 0 1 -1,1 A10,10 0 0 1 1,2 a1,1 0 0 1 1,-1 Z"/></svg>
    <span>(800) 555-0147</span>
  </div>
  <div class="contact" style="left:314px;top:168px">
    <svg width="13" height="13" viewBox="0 0 13 13" fill="none" stroke="#fff" stroke-width="1"><circle cx="6.5" cy="6.5" r="5.5"/><ellipse cx="6.5" cy="6.5" rx="2.5" ry="5.5"/><line x1="1" y1="6.5" x2="12" y2="6.5"/></svg>
    <span>drolbix.com<br>support@drolbix.com</span>
  </div>
  <footer class="foot"><div class="foot-brand"><i></i>Drolbix</div><div class="foot-url">Drolbix.com</div><div class="foot-page">Page No : 08</div></footer>
</section>

</body>
</html>
```